ONE PAGE WEB DESIGN NEEDED for Finance Company

We need a web design (ONE PAGE DESIGN ONLY) for a new finance website called Brightwell Lending. Brightwell Lending helps customers get the right loan, whether its a home loan, investment loan, business loan etc.

You are required to come up with just the homepage design. Professionalism and quality is the key factors in the successful design.

Here are a few design questions to help you out:

-
What information should be used on the page?
Ive provided a document which outlines all the information needed to put on homepage (attached to the brief - called brightwell_page_info). Also see the Must Have section below on this brief.

-
What links should appear in the navigation/footer?:
The navigation should provide links to the following pages (NOTE: services link has subcategories):
1 Homepage
2 Services
- Home loans
- Investment loans
- Refinancing loans
- Business loans
3 About Us
4 FAQ
5 Contact Us

-
What colors should be used in the design?
Our company colors - Cyan: #2EADE3, Blue: #004B70, White. Feel free to submit designs with slight variations if you feel it improves the design.

-
What should the layout of the page be?
This is up to you to come up with - we are open to different layouts for the page design (as long as they capture the information effectively and making it easy to understand).

Target Market(s)

Potential Home owners, Families and Business Owners

Industry/Entity Type

Business

Requirements
Must have
• - Must contain our logo (attached as PNG and Illustrator file)
- Winning designer must supply a Photoshop file (PSD) that will allow us.
Nice to have
• - Should include photos/images of families, professional groups, tradespeople etc (you can use stock photos from PixQuarry and I will purchase them once you are selected as the winning design)
- Link to a loan calculator somewhere on front page with a button 'Find out how much you could borrow' (or maybe even try adding a loan calculator to the homepage if you think this would look good)
- Page should have a main headline "Finding the right loan for you" or "Brightwell Lending finds the right loan for our customers."
- Must include Accreditation logos somewhere on the homepage (will try and supply these soon)
Should not have
• - Poor quality designs will not be considered
- Do not use clipart

```html
<!DOCTYPE html>
<html lang="en">
<head>
<meta charset="utf-8">
<title>Brightwell Lending – Home</title>
<link href="https://fonts.googleapis.com/css2?family=Arimo:wght@400;700&family=Open+Sans:wght@400;600&display=swap" rel="stylesheet">
<style>
:root{
  --cyan:#1aaae2;
  --cyan-mid:#0a99cc;
  --blue:#004b70;
  --blue-text:#0b5c86;
  --ink:#444;
  --pale:#b5f4fd;
  --field:#dcfbff;
  --field-line:#7fd8ee;
  --white:#fff;
}
*{box-sizing:border-box;margin:0;padding:0}
html,body{width:1200px;height:1097px;overflow:hidden;background:var(--white)}
body{font-family:"Arimo",Arial,sans-serif;color:var(--ink)}
.page{position:relative;width:1280px;height:1170px;transform:scale(.9375);transform-origin:0 0}
.abs{position:absolute}

.topbar{left:0;top:0;width:1280px;height:30px;background:var(--cyan);color:var(--white);font-size:12px}
.topbar .left{left:142px;top:8px}
.topbar .right{right:144px;top:8px;font-weight:700}
.topbar .right span{font-weight:400;color:#e6f7ff}
.sep{margin:0 9px}

.brand{left:143px;top:118px;display:flex;align-items:center;gap:10px;font-size:32px;color:var(--cyan);font-weight:700;letter-spacing:-.5px}
.brand i{display:block;width:22px;height:22px;border-radius:50%;background:var(--blue)}

.findus{left:896px;top:95px;font-size:15px;font-weight:700;color:var(--blue-text)}
.social{top:84px;width:41px;height:41px;border-radius:7px;display:flex;align-items:flex-end;justify-content:center;font-size:8px;color:var(--white);padding-bottom:4px}
.s1{left:1000px;background:#3b5b9c}.s2{left:1048px;background:#3fb6e8}.s3{left:1096px;background:#c9302c}

.tab{width:37px;background:var(--cyan)}
.tab span{position:absolute;left:50%;top:50%;transform:translate(-50%,-50%) rotate(-90deg);white-space:nowrap;color:var(--white);font-size:18px;letter-spacing:.3px}

.nav{left:177px;top:177px;width:162px}
.nav li{list-style:none;height:45px;background:var(--cyan);border-bottom:1px solid var(--white);color:var(--white);font-size:12px;padding:16px 0 0 13px;position:relative}
.nav li.current{color:var(--blue)}
.nav li .caret{position:absolute;right:12px;top:18px;width:0;height:0;border-left:5px solid var(--white);border-top:4px solid transparent;border-bottom:4px solid transparent}

.panel{left:176px;width:163px;background:var(--pale)}
.quote{padding:18px 0 0 10px;font-size:12px;color:#222}
.quote .intro{font-weight:700;color:var(--blue);line-height:18px;margin-bottom:5px}
.quote label{display:block;margin-bottom:6px}
.quote .field{width:132px;height:22px;background:var(--field);border:1px solid var(--field-line);margin-bottom:9px;position:relative}
.quote .field:after{content:"*";position:absolute;left:136px;top:4px;font-size:11px}
.quote .msg{width:142px;height:56px;background:var(--field);border:1px solid var(--field-line);margin-bottom:8px}
.btn{display:inline-block;width:52px;height:28px;border:1px solid #a9a9a9;background:#e6e6e6;font-size:14px;color:#111;text-align:center;line-height:26px;margin-right:4px}
.testimonial{padding:20px 12px 0 10px;font-family:"Open Sans",Arial,sans-serif;font-size:12.5px;line-height:18px;color:#333}
.testimonial b{font-weight:400;font-family:"Arimo",Arial,sans-serif;color:#222}

.slider-img{left:396px;top:183px;width:701px;height:248px;background:linear-gradient(115deg,#0f5f96 0%,#3b8cd0 30%,#a6d3f3 60%,#e4f2fc 100%)}
.arrow{top:292px;color:var(--white);font-size:34px;font-weight:700}

.welcome{left:359px;top:462px;width:547px;border-bottom:1px solid var(--cyan);padding-bottom:6px;font-size:25px;color:#444}
.welcome strong{font-weight:400;color:var(--blue-text)}
.copy{font-size:13px;line-height:18px;color:var(--ink)}
.copy p{margin-bottom:18px}

.side{left:926px;top:448px;width:214px}
.side div{height:30px;border-bottom:1px solid var(--white);padding-left:11px;color:var(--white)}
.side .head{background:var(--blue);font-size:17px;line-height:29px}
.side .item{background:var(--cyan-mid);font-size:13px;line-height:28px}

.offer{left:359px;top:692px;width:781px;height:239px;border:1px solid var(--cyan)}
.offer h3{position:absolute;left:11px;top:17px;font-size:13px;color:var(--blue)}
.col{position:absolute;top:44px;width:180px;font-size:13px;color:var(--blue-text)}
.col .pill{height:36px;border-radius:8px 8px 0 0;background:linear-gradient(#37bdf0,#1aa7e0 60%,#8fd9f6);color:var(--white);font-size:16px;padding:9px 0 0 11px}
.col .fade{height:22px;background:linear-gradient(#e7f6fc,#fff)}
.col ul{list-style:none;margin-top:-13px;padding-left:11px}
.col li{height:30px}
.col .sub{color:#333;font-weight:700;font-size:13.5px;height:27px}

.footer-line{left:140px;top:1057px;width:1000px;height:1px;background:var(--cyan)}
.footnav{left:142px;top:1069px;font-size:11px;color:var(--cyan)}
.footnav .sep{color:#555}
.copyright{left:142px;top:1087px;font-size:11px;color:#333}
.accept{left:972px;top:1074px;font-size:11px;color:#333}
.card{top:1069px;height:24px;border:1px solid #aaa;font-size:8px;color:var(--white);text-align:center;line-height:22px}
</style>
</head>
<body>
<div class="page">

  <header class="abs topbar">
    <div class="abs left">Welcome!<span class="sep">|</span>Our Location<span class="sep">|</span>Contact Us</div>
    <div class="abs right">E-mail: <span>info@brightwelllending.com.au</span><span class="sep">|</span>Call us &nbsp;today on: 1800 555 010</div>
  </header>

  <div class="abs brand"><i></i>Brightwell Lending</div>

  <div class="abs findus">FIND US ON :</div>
  <div class="abs social s1">Linkhub</div>
  <div class="abs social s2">Chatter</div>
  <div class="abs social s3">Reelcast</div>

  <!-- Quick links -->
  <svg class="abs" style="left:140px;top:177px" width="37" height="226" aria-hidden="true"><polygon points="0,0 37,0 37,226 0,190" fill="#1aaae2"/></svg>
  <div class="abs tab" style="left:140px;top:177px;height:190px;background:none"><span>QUICK LINKS</span></div>
  <ul class="abs nav">
    <li class="current">HOME PAGE</li>
    <li>SERVICES<span class="caret"></span></li>
    <li>ABOUT US</li>
    <li>FAQ</li>
    <li>CONTAT US</li>
  </ul>

  <!-- Quote form -->
  <svg class="abs" style="left:140px;top:412px" width="37" height="387" aria-hidden="true"><polygon points="0,0 37,0 37,387 0,352" fill="#1aaae2"/></svg>
  <div class="abs tab" style="left:140px;top:412px;height:352px;background:none"><span>GET A FREE QUOTE</span></div>
  <form class="abs panel quote" style="top:412px;height:387px">
    <p class="intro">Fill in your details below<br>&amp; we will contact you<br>within 24 hours:</p>
    <label>Full Name (required)</label><div class="field"></div>
    <label>Email (required)</label><div class="field"></div>
    <label>Phone (required)</label><div class="field"></div>
    <label>Address (required)</label><div class="field"></div>
    <label>Message:</label><div class="msg"></div>
    <span class="btn">Reset</span><span class="btn">Submit</span>
  </form>

  <!-- Testimonials -->
  <svg class="abs" style="left:140px;top:809px" width="37" height="238" aria-hidden="true"><polygon points="0,0 37,0 37,238 0,202" fill="#1aaae2"/></svg>
  <div class="abs tab" style="left:140px;top:809px;height:202px;background:none"><span>TESTIMONIALS</span></div>
  <div class="abs panel testimonial" style="top:809px;height:238px">
    Lorem ipsum dolor sit amet, consectetuer adipi-scing elit. Lorem ipsum dolor sit amet, con-sectetuer adipiscing elit. Lorem ipsum dolor sit amet, consectetuer adipi-scing elit. Lorem ipsum dolor sit amet, con-sectetuer adipiscing elit<br><b>- Maya and Tom</b>
  </div>

  <!-- Slider -->
  <svg class="abs" style="left:359px;top:177px" width="781" height="261" aria-hidden="true">
    <polygon points="0,0 37,0 37,261 0,225" fill="#1aaae2"/>
    <polygon points="744,0 781,36 781,261 744,261" fill="#1aaae2"/>
    <rect x="37" y="0" width="707" height="261" fill="#0d6a96"/>
  </svg>
  <div class="abs slider-img" role="img" aria-label="Close-up photo of a pen resting on a financial chart"></div>
  <div class="abs arrow" style="left:367px">&#10094;</div>
  <div class="abs arrow" style="left:1112px">&#10095;</div>

  <!-- Welcome -->
  <h1 class="abs welcome">Welcome to <strong>BRIGHTWELL LENDING!!</strong></h1>
  <div class="abs copy" style="left:359px;top:510px;width:550px">
    <p>At Brightwell Lending we work hard to find the right loan for our customers. We do that because we are backed by sound industry knowledge, professional experience and a great customer service approach.</p>
    <p>Brightwell Lending guarantees that we will always tailor the best solution for your individual lending needs.</p>
    <p>We can do that because we have access to a wide variety of lending options from major banks to non-bank lenders and we are committed to finding the right lending product for you.</p>
  </div>

  <nav class="abs side">
    <div class="head">Forms &amp; brochures:</div>
    <div class="item">Investments</div>
    <div class="item">Retirement income</div>
    <div class="head">Advice information:</div>
    <div class="item">Retire with more</div>
    <div class="item">Advice makes a difference</div>
    <div class="head">Annual reports:</div>
  </nav>

  <!-- Offer -->
  <section class="abs offer">
    <h3>We offer a unique approach to help you find the right:</h3>
    <div class="col" style="left:9px"><div class="pill">Home Loan</div><div class="fade"></div>
      <ul><li>+ Home buyers</li><li>+ First home buyers</li><li>+ Over 20 lenders</li></ul></div>
    <div class="col" style="left:202px"><div class="pill">Investment Loan</div><div class="fade"></div>
      <ul><li>+ Property investment loans</li><li>+ Interest only loans</li></ul></div>
    <div class="col" style="left:396px"><div class="pill">Refinancing</div><div class="fade"></div>
      <ul style="padding-left:2px"><li>+ Refinancing for the best rate</li><li>+ Upsizing or downsizing</li><li>+ Change from a variable</li><li style="padding-left:11px">to a &nbsp;fixed rate</li></ul></div>
    <div class="col" style="left:589px"><div class="pill">Business Loan</div><div class="fade"></div>
      <ul><li class="sub">Business Finance</li><li>+ Long term</li><li>+ Short term</li><li>+ Equipment and Leasing</li></ul></div>
  </section>

  <div class="abs copy" style="left:359px;top:950px;width:780px">
    <p>There are many different loan products in the marketplace. Brightwell Lending has access to a wide panel of lenders which means we can access bank and non-bank lenders that meet the individual needs of our customers.</p>
    <p>Contact Brightwell Lending today on: 1800 555 010 to find out more.</p>
  </div>

  <!-- Footer -->
  <div class="abs footer-line"></div>
  <div class="abs footnav">Home Page<span class="sep">|</span>Services<span class="sep">|</span>About Us<span class="sep">|</span>FAQ<span class="sep">|</span>Contact Us</div>
  <div class="abs copyright">Copyright © 2012. Brightwell Lending. All Rights reserved.</div>
  <div class="abs accept">We Accept:</div>
  <div class="abs card" style="left:1038px;width:35px;background:#1a3f8f">Paylo</div>
  <div class="abs card" style="left:1074px;width:35px;background:#d8452b">Cardeo</div>
  <div class="abs card" style="left:1110px;width:28px;background:#2e77bb">Expra</div>

</div>
</body>
</html>
```